Parody of energy drink Grizzle Hyper Nil

We need an energy drink designed that is extremely similar to Grizzle Hyper Nil in color and design. We also need a similar name/logo (but not identical). If it's a funny/sarcastic/parody name, even better. We're open to naming options.

This will NOT be used on physical products, it's for a virtual 3D item in a web game.

Can is 500ml in size.

Colors
ffffff

```html
<!DOCTYPE html>
<html lang="en">
<head>
<meta charset="utf-8">
<title>Grizzloon Energy Hyper Nil – Can Label</title>
<link rel="stylesheet" href="https://fonts.googleapis.com/css2?family=Cinzel:wght@500;700&family=Saira:wght@400;700&display=swap">
<style>
  :root {
    --backdrop: #edf0f4;
    --label-white: #ffffff;
    --label-shade: #e4e4e4;
    --swirl-tone: #dcdcdc;
    --ink: #111111;
    --energy-blue: #2f86b5;
    --mark-grey: #7a7a7a;
  }
  html, body {
    margin: 0;
    width: 1200px;
    height: 960px;
    overflow: hidden;
    background: var(--backdrop);
  }
  .canvas {
    position: relative;
    width: 1200px;
    height: 960px;
  }
  .can-label {
    position: absolute;
    left: 471px;
    top: 156px;
    width: 254px;
    height: 645px;
    background: var(--label-white);
    overflow: hidden;
  }
  .ornament-field {
    position: absolute;
    inset: 0;
    background:
      linear-gradient(90deg, var(--label-shade) 0%, transparent 18%, transparent 82%, var(--label-shade) 100%),
      linear-gradient(160deg, var(--swirl-tone) 0%, var(--label-white) 30%, var(--swirl-tone) 55%, var(--label-white) 75%, var(--swirl-tone) 100%);
  }
  .ingredients {
    position: absolute;
    top: 17px;
    left: 0;
    right: 0;
    text-align: center;
    font-family: "Cinzel", serif;
    font-weight: 500;
    font-size: 11px;
    letter-spacing: 6px;
    color: var(--ink);
    white-space: nowrap;
  }
  .brand-disc {
    position: absolute;
    left: 50%;
    top: 150px;
    width: 180px;
    height: 180px;
    margin-left: -90px;
    border-radius: 50%;
    background: var(--mark-grey);
  }
  .brand-name {
    position: absolute;
    top: 414px;
    left: 0;
    right: 0;
    margin: 0;
    text-align: center;
    font-family: "Cinzel", serif;
    font-weight: 700;
    font-size: 37px;
    line-height: 1;
    letter-spacing: 0;
    color: var(--ink);
    white-space: nowrap;
  }
  .energy {
    position: absolute;
    top: 478px;
    left: 0;
    right: 0;
    text-align: center;
    font-family: "Saira", sans-serif;
    font-weight: 700;
    font-size: 30px;
    line-height: 1;
    letter-spacing: 21px;
    padding-left: 21px;
    color: var(--energy-blue);
  }
  .variant {
    position: absolute;
    top: 522px;
    left: 0;
    right: 0;
    text-align: center;
    font-family: "Saira", sans-serif;
    font-weight: 700;
    font-size: 22px;
    line-height: 1.2;
    color: var(--ink);
  }
  .volume {
    position: absolute;
    top: 569px;
    left: 0;
    right: 0;
    text-align: center;
    font-family: "Saira", sans-serif;
    font-weight: 400;
    font-size: 21px;
    line-height: 1.2;
    color: var(--ink);
  }
</style>
</head>
<body>
  <main class="canvas">
    <section class="can-label">
      <div class="ornament-field" role="img" aria-label="Soft grey baroque swirl pattern across the white label"></div>
      <div class="ingredients">TAURIN + GINSENG</div>
      <div class="brand-disc"></div>
      <h1 class="brand-name">GRIZZLOON</h1>
      <div class="energy">ENERGY</div>
      <div class="variant">HYPER NIL</div>
      <div class="volume">500 mL</div>
    </section>
  </main>
</body>
</html>
```